New Summit Tile Billboard at HQ

Looking to design a catchy image / theme for a billboard located just above our corporate HQ showroom and warehouse, along the service road of a 6-lane highway. Billboard measures 8ft x 24 ft. Would like to highlight that the store location is directly beneath the sign.

We are a retail and wholesale business selling premium flooring, ready to assemble cabinets, and granite countertops. See image ideas attached. Our information:
NAME: Summit Tile, Cabinets, Countertops
ADDRESS: 417 W. Hwy 82, Duncanville, TX 75284
WEBSITE: www.summittilehub.example
PHONE: 972-8-TILEUP (972-845-3887)

```html
<!DOCTYPE html>
<html lang="en">
<head>
<meta charset="utf-8">
<title>Summit Tile Billboard</title>
<link rel="stylesheet" href="https://fonts.googleapis.com/css2?family=Montserrat:wght@600;700;800&display=swap">
<style>
  :root {
    --green: #7dc242;
    --red: #e3263a;
    --ink: #141414;
    --white: #ffffff;
    --page: #e6e6e6;
  }
  html, body { margin: 0; padding: 0; overflow: hidden; }
  body {
    width: 1200px; height: 1091px;
    background: var(--page);
    font-family: "Montserrat", sans-serif;
    position: relative;
  }
  .billboard {
    position: absolute; left: 30px; top: 355px;
    width: 1140px; height: 380px;
    box-shadow: 0 10px 24px rgba(0,0,0,.35);
    overflow: hidden;
  }
  .billboard-shapes { position: absolute; inset: 0; }
  .tag {
    position: absolute; top: 6px;
    color: var(--white); font-weight: 800; font-size: 29px; letter-spacing: .5px;
  }
  .tag--before { left: 125px; }
  .tag--after { left: 955px; }
  .brand {
    position: absolute; left: 0; width: 1124px; top: 28px;
    display: flex; justify-content: center; align-items: center; gap: 8px;
  }
  .brand-dot { width: 22px; height: 22px; border-radius: 50%; background: var(--green); }
  .brand-name { font-weight: 800; font-size: 38px; color: var(--ink); line-height: 1; }
  .services { position: absolute; top: 104px; left: 0; }
  .service {
    position: absolute; transform: translateX(-50%);
    display: flex; flex-direction: column; align-items: center;
  }
  .service svg { width: 38px; height: 38px; }
  .service-label { margin-top: 6px; font-weight: 800; font-size: 19px; color: var(--ink); white-space: nowrap; }
  .divider { position: absolute; top: 108px; width: 1px; height: 68px; background: #9a9a9a; }
  .headline {
    position: absolute; left: 0; width: 1128px; top: 180px;
    text-align: center; font-weight: 800; white-space: nowrap; line-height: 1;
  }
  .headline-lead { font-size: 34px; color: var(--ink); }
  .headline-key { font-size: 49px; color: var(--green); }
  .phone {
    position: absolute; left: 412px; top: 247px;
    font-weight: 800; font-size: 18.5px; color: var(--ink); white-space: nowrap;
  }
  .web {
    position: absolute; left: 372px; top: 292px;
    display: flex; align-items: center; gap: 9px;
    font-weight: 600; font-size: 19px; color: var(--white); letter-spacing: .4px; white-space: nowrap;
  }
  .web strong { color: var(--green); font-weight: 800; }
  .address {
    position: absolute; left: 308px; top: 342px;
    display: flex; align-items: center; gap: 8px;
    font-weight: 700; font-size: 19.5px; color: var(--ink); white-space: nowrap;
  }
</style>
</head>
<body>
<section class="billboard">
  <svg class="billboard-shapes" viewBox="0 0 1140 380" width="1140" height="380">
    <defs>
      <linearGradient id="beforeTone" x1="0" y1="0" x2="0" y2="1">
        <stop offset="0" stop-color="#e6cfc0"/>
        <stop offset=".6" stop-color="#d2bfae"/>
        <stop offset="1" stop-color="#b9a58e"/>
      </linearGradient>
      <linearGradient id="afterTone" x1="0" y1="0" x2="0" y2="1">
        <stop offset="0" stop-color="#fbe0b8"/>
        <stop offset=".55" stop-color="#f2cc9b"/>
        <stop offset=".7" stop-color="#c97b3e"/>
        <stop offset="1" stop-color="#b9662c"/>
      </linearGradient>
      <linearGradient id="edgeFade" x1="0" y1="1" x2="0" y2="0">
        <stop offset="0" stop-color="#7dc242"/>
        <stop offset="1" stop-color="#7dc242" stop-opacity="0"/>
      </linearGradient>
    </defs>
    <rect width="1140" height="380" fill="#ffffff"/>
    <polygon points="0,0 392,0 281,380 0,380" fill="url(#beforeTone)" role="img" aria-label="Photo of a bare, worn room before renovation"/>
    <polygon points="856,0 1140,0 1140,380 750,380" fill="url(#afterTone)" role="img" aria-label="Photo of the same room after renovation with new wood floor"/>
    <polygon points="392,0 404,0 293,380 281,380" fill="#7dc242"/>
    <polygon points="844,0 856,0 750,380 738,380" fill="url(#edgeFade)"/>
    <polygon points="95,0 285,0 272,42 122,42" fill="#e3263a"/>
    <polygon points="925,0 1110,0 1083,42 938,42" fill="#e3263a"/>
    <polygon points="316,258 783,258 764,328 296,328" fill="#141414"/>
    <rect x="384" y="241" width="346" height="37" rx="18.5" fill="#7dc242"/>
    <circle cx="386" cy="259" r="17" fill="#141414" stroke="#ffffff" stroke-width="2"/>
    <path d="M380 251c2-1 3 0 4 2l1 3-2 2c1 2 3 4 5 5l2-2 3 1c2 1 3 2 2 4l-1 2c-7 0-14-7-15-14z" fill="#ffffff"/>
  </svg>

  <div class="tag tag--before">BEFORE</div>
  <div class="tag tag--after">AFTER</div>

  <div class="brand">
    <span class="brand-dot"></span>
    <span class="brand-name">Summit Tile</span>
  </div>

  <div class="services">
    <div class="service" style="left:409px">
      <svg viewBox="0 0 38 38"><circle cx="19" cy="19" r="17" fill="none" stroke="#7dc242" stroke-width="2"/><rect x="11" y="11" width="16" height="16" fill="none" stroke="#333" stroke-width="1.6"/><path d="M11 19l8-8M11 25l14-14M15 27l12-12M21 27l6-6" stroke="#333" stroke-width="1.2"/></svg>
      <span class="service-label">FLOOR</span>
    </div>
    <div class="service" style="left:530px">
      <svg viewBox="0 0 38 38"><circle cx="19" cy="19" r="17" fill="none" stroke="#7dc242" stroke-width="2"/><rect x="12" y="10" width="14" height="18" rx="1.5" fill="none" stroke="#333" stroke-width="1.6"/><path d="M12 16h14M12 22h14M17 13h4M17 19h4M17 25h4" stroke="#333" stroke-width="1.4"/></svg>
      <span class="service-label">CABINETS</span>
    </div>
    <div class="service" style="left:689px">
      <svg viewBox="0 0 38 38"><circle cx="19" cy="19" r="17" fill="none" stroke="#7dc242" stroke-width="2"/><path d="M9 16h20" stroke="#333" stroke-width="1.8"/><rect x="11" y="18" width="16" height="9" fill="none" stroke="#333" stroke-width="1.6"/><path d="M19 18v9M13 12h3M22 12h3" stroke="#333" stroke-width="1.4"/></svg>
      <span class="service-label">COUNTERTOPS</span>
    </div>
  </div>
  <span class="divider" style="left:464px"></span>
  <span class="divider" style="left:596px"></span>

  <div class="headline"><span class="headline-lead">NEED AN </span><span class="headline-key">UPDATE?</span></div>

  <div class="phone">972-8-TILEUP (972-845-3887)</div>

  <div class="web">
    <svg width="18" height="18" viewBox="0 0 20 20"><circle cx="10" cy="10" r="8.5" fill="none" stroke="#fff" stroke-width="1.6"/><ellipse cx="10" cy="10" rx="3.6" ry="8.5" fill="none" stroke="#fff" stroke-width="1.3"/><path d="M2 10h16M3.5 6h13M3.5 14h13" stroke="#fff" stroke-width="1.2"/></svg>
    <span>WWW.<strong>SUMMITTILEHUB</strong>.EXAMPLE</span>
  </div>

  <div class="address">
    <svg width="18" height="22" viewBox="0 0 18 22"><path d="M9 1a7 7 0 0 1 7 7c0 5-7 13-7 13S2 13 2 8a7 7 0 0 1 7-7z" fill="none" stroke="#e3263a" stroke-width="2"/><circle cx="9" cy="8" r="2.5" fill="#e3263a"/></svg>
    <span>417 W. Hwy 82, Duncanville, TX 75284</span>
  </div>
</section>
</body>
</html>
```